Golden Years Wellness Roadmap: This is my second book. The first was Eldercare Compass

I need a book cover design for: GOLDEN YEARS WELLNESS ROADMAP: A NO-EXPENSE METHOD FOR FINISHING YOUR LATER-LIFE MOSAIC WITH POOLED KVB CARE SCHEMES by Derek Holloway Neil Osgrove & Martin Quarles. This book is designed for business owners, CEO's, CFO's and Human Resources. The cover needs to be professional and focused on business. The purpose of this book is to educate business owners and their management about a zero cost retiree health plan. This is a first of it's kind solution that every business needs to learn about.

Target Market(s)

Business owners, CEO's, CFO's and Human Resources

Requirements
Nice to have
• I want the design to be clean and professional since it is focused on business executives

```html
<!DOCTYPE html>
<html lang="en">
<head>
<meta charset="utf-8">
<title>Golden Years Wellness Roadmap — Book Cover</title>
<link rel="stylesheet" href="https://fonts.googleapis.com/css2?family=Barlow:wght@400;500;600&family=Barlow+Condensed:wght@500;600&display=swap">
<style>
  :root {
    --paper: #ffffff;
    --accent-blue: #1a9bd0;
    --subtitle-grey: #6f7173;
    --title-green-light: #6fcf97;
    --title-green-dark: #4aaf85;
    --title-blue-light: #3fc5ee;
    --title-blue-dark: #2a9fcb;
    --author-ink: #111111;
    --art-sky: #eaf6fc;
    --art-blue: #3cc6f2;
    --art-green: #7fd49a;
    --art-gold: #f6cd3c;
  }
  * { margin: 0; padding: 0; box-sizing: border-box; }
  html, body { width: 800px; height: 1200px; overflow: hidden; background: var(--paper); }
  .cover {
    position: relative;
    width: 800px;
    height: 1200px;
    background: var(--paper);
    font-family: "Barlow", Arial, sans-serif;
    text-align: center;
  }
  .subtitle {
    position: absolute;
    top: 62px;
    left: 0;
    width: 100%;
    font-size: 22.5px;
    line-height: 34px;
    font-weight: 400;
    color: var(--subtitle-grey);
    text-transform: uppercase;
  }
  .subtitle-lead { color: var(--accent-blue); font-weight: 600; }
  .hero-art {
    position: absolute;
    top: 195px;
    left: 110px;
    width: 590px;
    height: 525px;
  }
  .title {
    position: absolute;
    left: 0;
    width: 100%;
    font-family: "Barlow Condensed", "Arial Narrow", sans-serif;
    text-transform: uppercase;
    line-height: 1;
  }
  .title-top {
    top: 783px;
    font-size: 78px;
    font-weight: 600;
    letter-spacing: -0.5px;
    background: linear-gradient(90deg, var(--title-green-light), var(--title-green-dark));
    -webkit-background-clip: text;
    background-clip: text;
    color: transparent;
  }
  .title-main {
    top: 862px;
    font-size: 206px;
    font-weight: 500;
    letter-spacing: 4px;
    background: linear-gradient(90deg, var(--title-blue-dark), var(--title-blue-light) 50%, var(--title-blue-dark));
    -webkit-background-clip: text;
    background-clip: text;
    color: transparent;
  }
  .authors {
    position: absolute;
    top: 1074px;
    left: 0;
    width: 100%;
    font-size: 23px;
    line-height: 34px;
    font-weight: 600;
    letter-spacing: 3.2px;
    color: var(--author-ink);
    text-transform: uppercase;
  }
</style>
</head>
<body>
  <main class="cover">
    <p class="subtitle">
      <span class="subtitle-lead">A No-Expense Method</span><br>
      For Finishing Your Later-Life<br>
      Mosaic With Pooled KVB Care Schemes
    </p>

    <svg class="hero-art" viewBox="0 0 590 525" role="img" aria-label="Illustration of an insurance document with a winged medical staff, a stack of banknotes, gold coins and a health card">
      <defs>
        <radialGradient id="art-glow" cx="50%" cy="48%" r="55%">
          <stop offset="0%" stop-color="var(--art-sky)"/>
          <stop offset="100%" stop-color="#f7fbfe"/>
        </radialGradient>
        <linearGradient id="art-tones" x1="0" y1="0" x2="1" y2="0">
          <stop offset="0%" stop-color="var(--art-blue)" stop-opacity="0.35"/>
          <stop offset="60%" stop-color="var(--art-green)" stop-opacity="0.35"/>
          <stop offset="100%" stop-color="var(--art-gold)" stop-opacity="0.35"/>
        </linearGradient>
      </defs>
      <circle cx="295" cy="255" r="280" fill="url(#art-glow)"/>
      <rect x="60" y="145" width="470" height="365" rx="24" fill="url(#art-tones)"/>
      <line x1="0" y1="515" x2="590" y2="515" stroke="#1f3b57" stroke-width="2" stroke-dasharray="40 6 10 6"/>
    </svg>

    <h1>
      <span class="title title-top">Golden Years Wellness</span>
      <span class="title title-main">Roadmap</span>
    </h1>

    <p class="authors">Derek Holloway, Neil Osgrove<br>Martin Quarles</p>
  </main>
</body>
</html>
```